Web Design Project: Facility Management company

Hi! We need a new website.

Our current website: http://www.vireo-trade.ru/ and we don-t like it. =)
The structure of our company has changed and now we don't need "cleaning" and "engeneering" on this site.

We are facility management company in Russia. So we provide integrated service solutions specific to industrial services: maintenance, repair, etc. of engineering systems.
More services:
Energy planning
Automation
Audit
Statements with regulators
Video surveillance
Central heating
Security systems
Welding
Management of subcontractors
Electrical installation and service needs
Reception
Catering

Visitors:
* Managers in the field of commercial real estate
* Chief engineers
* TOP managers of large companies, malls, factories...
+ their subordinates
* Small% of applicants.

Here you can see some websites/patterns we liked:
http://www.kobalmire.ru/ (This is our competitor’s site, so our site shouldn’t be an exact copy))))
http://www.dwatqo.ru/
http://www.layoutfarrow.com/demo/24296.html
http://www.layoutfarrow.com/website-templates/10145.html

Style:
Light, hi-tech/minimalizm, the color palette should be based on the original site colors (Green + black + white). http://www.vireo-trade.ru/

Estimated sitemap:
1. Home
2. About Us
3. Company's policy
4. History + Achievements.
5. Certificates
6. Map of presence (Here you can use sample map in file "our projects")
7. Services
8. Portfolio
9. News or blog
10. Jobs
11. Contacts - with the feedback form (or the function "call to order")
12. English

Need a design pages: main page, page 404. The rest of the page could be created by general pattern.

Logo, navigation bar and contacts should be visible on all pages of a site.
Flash animation elements and buttons, etc. - not needed.

* We need to develop 3 websites, so we are looking for a long term cooperation.
Looking forward to your creativity =)

Must Have:
Clear, intuitive structure of web pages.
In the center - of pictures reflecting our main services (industrial theme). May be in rotation.
BUT! This banner (central picture) should not be a huge one =)
All relevant information should be visible at once without scrolling.

A possibility to place media files (presentations, video ...) and 2 banner links on the main page.

Font should be available in Cyrillic.
Updates

IMPORTANT!

Please notice that in thisdesign we don't need "cleaning" and "engeneering" on this site.

So don't use old block of 4pictures from our current website. We don't need it anymore. 

Thestructure of our company has changed and now we need some links (may be banners,may be something else) to our future cleaning website as well as engeneeringwebsite.
It should look like seperate (partner) companies, not like our sevices.

Regards, Vera.

Please don't forget that we need bilingual site.

So define language changing tool in your designs.

Industry/Entity Type

Industrial

```html
<!DOCTYPE html>
<html lang="en">
<head>
<meta charset="utf-8">
<title>Vireo Trade — Facility Management</title>
<link rel="stylesheet" href="https://fonts.googleapis.com/css2?family=Noto+Sans:wght@400;700&family=Arimo:wght@400;700&display=swap">
<style>
:root{
  --dark:#1e1f1e;
  --green:#86a02e;
  --green-deep:#7b952a;
  --lime:#a6c43a;
  --lime-bright:#c4dc55;
  --white:#ffffff;
  --black:#000000;
  --muted:#a9bd6a;
}
*{box-sizing:border-box;margin:0;padding:0}
html,body{width:1200px;height:900px;overflow:hidden}
body{position:relative;background:var(--green);font-family:"Noto Sans",Verdana,sans-serif;color:var(--white)}
a{color:inherit}
.abs{position:absolute}
.top-band{left:0;top:0;width:1200px;height:321px;
  background:radial-gradient(ellipse at 45% 10%,#3b3d3a 0%,transparent 55%),
  linear-gradient(180deg,#262725 0%,#1b1c1b 100%);border-top:3px solid var(--lime)}
.top-strip{left:0;top:32px;width:1200px;height:75px;
  background:linear-gradient(180deg,#3a3a39 0%,#6b6b6a 45%,#3a3a39 100%);opacity:.7}
.search-bar{left:48px;top:48px;width:1080px;height:28px;border-radius:6px;
  background:linear-gradient(180deg,#8f8f8e,#6c6c6b);opacity:.55}
.brand{left:372px;top:10px;width:400px;height:100px;border-radius:8px;
  background:radial-gradient(ellipse at center,#d7d7d5 0%,#a9a9a7 60%,rgba(120,120,118,0) 100%);
  display:flex;align-items:center;justify-content:center;flex-direction:column}
.brand-name{font-size:38px;letter-spacing:6px;font-weight:400;color:#1a1a1a;line-height:1}
.brand-sub{font-size:15px;letter-spacing:5px;font-weight:400;color:#1a1a1a;margin-top:4px}
.lang{left:858px;top:18px;display:flex;align-items:center;gap:8px;font-weight:700;font-size:16px}
.icon-badge{width:36px;height:36px}
.phone-icon{left:225px;top:51px}
.phone{left:178px;top:96px;font-weight:700;font-size:15px;color:var(--lime-bright);
  text-shadow:0 0 2px #000,1px 1px 0 #000;white-space:nowrap}
.also{left:159px;top:186px;width:156px;text-align:center;font-size:21px;font-weight:700}
.partner-link{display:block;width:156px;height:23px;line-height:21px;text-align:center;text-decoration:none;
  font-family:Arimo,Arial,sans-serif;font-size:13px;font-weight:700;background:var(--lime);border:1px solid #c9de6b;white-space:nowrap}
.partner-link.cleaning{left:159px;top:221px;color:var(--white)}
.partner-link.engineering{left:159px;top:249px;color:#2d3a0a}
.thumb-icon{left:215px;top:305px}
.firm{left:150px;top:352px;width:166px;text-align:center;font-family:Arimo,Arial,sans-serif;font-weight:700;font-size:17px;line-height:19px}
.site-url{left:150px;top:425px;width:166px;text-align:center;font-family:Arimo,Arial,sans-serif;font-size:16px;font-weight:700;color:var(--muted)}
.promo{top:133px;width:234px;height:342px;background:var(--white);padding:5px;text-decoration:none;color:var(--white);
  box-shadow:0 0 6px rgba(0,0,0,.7)}
.promo.one{left:352px}.promo.two{left:593px}
.promo-photo{width:224px;height:255px;position:relative;display:flex;align-items:flex-end;justify-content:center;padding-bottom:4px}
.promo.one .promo-photo{background:linear-gradient(160deg,#dfeaf5 0%,#5e9dd6 45%,#1f5e9f 100%)}
.promo.two .promo-photo{background:linear-gradient(160deg,#d9d9d7 0%,#a7a8a6 60%,#8a8b89 100%)}
.promo-cta{font-weight:700;font-size:17px;line-height:19px;text-align:center;color:var(--white);
  text-shadow:0 0 2px #000,1px 1px 1px #000}
.promo-label{margin-top:5px;height:72px;background:var(--lime);display:flex;align-items:center;justify-content:center;
  text-align:center;font-weight:700;font-size:14px;line-height:19px;color:var(--white);text-decoration:underline;text-shadow:1px 1px 1px #566b12}
.nav-title{left:840px;top:126px;font-weight:700;font-size:24px}
.nav-title span{font-size:24px;color:#c9c9b8;text-shadow:0 0 2px #000}
.nav-rule{left:835px;top:162px;height:294px;border-left:3px dashed var(--white)}
.main-nav{left:849px;top:174px;list-style:none;font-family:Arimo,Arial,sans-serif}
.main-nav li{display:flex;align-items:center;height:24px;font-size:14px;font-weight:700;white-space:nowrap}
.main-nav li::before{content:"";width:14px;height:14px;margin-right:7px;background:#2a2b29;border:1px solid #555}
.main-nav li.on-green::before{background:#2e3814;border-color:#56682a}
.main-nav a{color:var(--white);text-decoration:underline}
.tagline{left:150px;top:494px;width:876px;text-align:center;font-weight:700;font-size:23px;line-height:23px;letter-spacing:.6px;white-space:nowrap;
  text-shadow:-1px -1px 0 #000,1px -1px 0 #000,-1px 1px 0 #000,1px 1px 0 #000}
.tagline em{font-style:normal;color:var(--lime)}
.dashes{left:438px;top:553px;width:292px;border-top:4px dashed var(--white)}
.keywords{left:145px;top:577px;width:891px;height:31px;border-radius:6px;background:#111;border:1px solid #777;
  display:flex;align-items:center;justify-content:center;font-family:Arimo,Arial,sans-serif;font-size:14px;font-weight:700;gap:8px;white-space:nowrap}
.section-title{left:0;top:648px;width:1182px;text-align:center;color:var(--black);font-weight:700;font-size:28px}
.col{top:692px;height:210px;background:var(--green-deep)}
.col.sub{left:145px;width:172px;padding:26px 8px}
.col.main{left:325px;width:484px;padding:26px 11px;font-family:Arimo,Arial,sans-serif;color:#111;font-size:12px;line-height:14px}
.col.side{left:816px;width:220px;padding:27px 14px;font-family:Arimo,Arial,sans-serif;color:#111;font-size:12px;line-height:14px;font-weight:700}
.sub h3{color:var(--black);font-size:19px;font-weight:700;margin-bottom:10px}
.sub ul{list-style:none;padding-left:16px;font-family:Arimo,Arial,sans-serif}
.sub li{height:24px;font-size:12px;font-weight:700;white-space:nowrap}
.sub a{color:var(--white)}
.main p{margin-bottom:14px}
.main h4{font-family:Arimo,Arial,sans-serif;font-size:13px;color:var(--white);margin-bottom:10px}
.side p{margin-bottom:14px}
.side ul{list-style:none;color:var(--white)}
.side li{height:18px}
</style>
</head>
<body>
<div class="abs top-band"></div>
<div class="abs top-strip"></div>
<div class="abs search-bar"></div>

<header>
  <div class="abs brand"><span class="brand-name">VIREO TRADE</span><span class="brand-sub">engineering systems</span></div>
  <div class="abs lang">
    <svg width="28" height="18" viewBox="0 0 28 18"><rect width="28" height="6" fill="#fff"/><rect y="6" width="28" height="6" fill="#1f45b5"/><rect y="12" width="28" height="6" fill="#d21c1c"/></svg>
    Русский
  </div>
  <svg class="abs icon-badge phone-icon" viewBox="0 0 36 36"><circle cx="18" cy="18" r="17" fill="#eee"/><circle cx="18" cy="18" r="13" fill="#8fae2f"/><path d="M13 10c2 0 3 4 2 5l-1 1c1 3 3 5 6 6l1-1c1-1 5 0 5 2 0 2-2 3-4 3-6 0-12-6-12-12 0-2 1-4 3-4z" fill="#fff"/></svg>
  <div class="abs phone">+ 7 812 555 0148</div>
</header>

<aside>
  <div class="abs also">Also visit</div>
  <a class="abs partner-link cleaning" href="#">Cleaning website</a>
  <a class="abs partner-link engineering" href="#">Engeneering website</a>
  <svg class="abs icon-badge thumb-icon" viewBox="0 0 36 36"><circle cx="18" cy="18" r="17" fill="#eee"/><circle cx="18" cy="18" r="13" fill="#8fae2f"/><path d="M11 16h4v10h-4zM16 16l4-7c2 0 2 2 2 3l-1 4h5c1 0 2 1 1 3l-2 6c0 1-1 1-2 1h-7z" fill="#fff"/></svg>
  <div class="abs firm">VIREO - TM - FM<br>company</div>
  <div class="abs site-url">vireo-trade.ru</div>
</aside>

<section>
  <a class="abs promo one" href="#">
    <div class="promo-photo" role="img" aria-label="Photo of a glass office tower reflecting blue sky and clouds"><span class="promo-cta">Click here to<br>learn more</span></div>
    <div class="promo-label">Integrated facility<br>management</div>
  </a>
  <a class="abs promo two" href="#">
    <div class="promo-photo" role="img" aria-label="Photo of white painted pipes on a textured wall"><span class="promo-cta">Click here to<br>learn more</span></div>
    <div class="promo-label">Technical maintenance of<br>engineering systems</div>
  </a>
</section>

<nav>
  <div class="abs nav-title">Our <span>Company</span></div>
  <div class="abs nav-rule"></div>
  <ul class="abs main-nav">
    <li><a href="#">Home</a></li>
    <li><a href="#">About Us</a></li>
    <li><a href="#">Company's policy</a></li>
    <li><a href="#">History + Achievements.</a></li>
    <li><a href="#">Certificates</a></li>
    <li><a href="#">Map of presence</a></li>
    <li class="on-green"><a href="#">Services</a></li>
    <li class="on-green"><a href="#">Portfolio</a></li>
    <li class="on-green"><a href="#">News or blog</a></li>
    <li class="on-green"><a href="#">Jobs</a></li>
    <li class="on-green"><a href="#">Contacts</a></li>
  </ul>
</nav>

<div class="abs tagline">A team of <em>specialists</em> for all your needs in<br>commercial property <em>management</em> and <em>maintenance</em></div>
<div class="abs dashes"></div>
<div class="abs keywords"><span>Commercial property management</span><span>-</span><span>Complex maintenance of immovable property</span><span>-</span><span>Commercial property maintenance service</span></div>

<h2 class="abs section-title">- Section Title Here -</h2>

<main>
  <div class="abs col sub">
    <h3>SubMenu</h3>
    <ul>
      <li><a href="#">Home</a></li>
      <li><a href="#">About Us</a></li>
      <li><a href="#">Company's policy</a></li>
      <li><a href="#">History + Achievements.</a></li>
      <li><a href="#">Certificates</a></li>
      <li><a href="#">Map of presence</a></li>
    </ul>
  </div>
  <div class="abs col main">
    <p>These are the most important aspects of acquisition of the highest possible incomes from the commercial property object`s operation regardless of their purpose: it can be production, business center, a building of a shop, bank, restaurant, warehousing logistic complex, hotel or the biggest shopping and recreation center.</p>
    <p>More and more modern companies – proprietors and developer companies, hand over maintenance of the buildings, structures with all installation for outsourcing to a professional management company.</p>
    <h4>Why do they choose us?</h4>
    <p>Following the complex approach to management problems, we will help to optimize maintenance costs and your immovable property service.</p>
  </div>
  <div class="abs col side">
    <p>We are facility management company in Russia. So we provide integrated service solutions specific to industrial services: maintenance, repair, etc. of engineering systems.</p>
    <p>Plus:</p>
    <ul>
      <li>- &nbsp;Energy planning</li>
      <li>- &nbsp;Automation</li>
      <li>- &nbsp;Audit</li>
    </ul>
  </div>
</main>
</body>
</html>
```